BRL business card

For a business card with our logo

Contact Information for Business Card

Mathéo VRANEL
Founder & CEO
email : ceo@brightlanterncollective.com / www.brightlanterncollective.com /
instagram / facebook / WhatsApp
N°: +590 690 482 517

Colors

Designer to choose colors to be used in the design.

```html
<!DOCTYPE html>
<html lang="en">
<head>
<meta charset="utf-8">
<title>BRL business card</title>
<link rel="stylesheet" href="https://fonts.googleapis.com/css2?family=Tinos:wght@400;700&display=swap">
<style>
  :root {
    --brand-blue: #1452a0;
    --brand-orange: #e4672a;
    --paper: #f3f3f2;
    --ink: #2e2e33;
    --white: #ffffff;
    --backdrop: #e8e5e0;
  }
  * { margin: 0; padding: 0; box-sizing: border-box; }
  html, body {
    width: 900px; height: 1200px; overflow: hidden;
    background: var(--backdrop);
    font-family: "Tinos", "Times New Roman", serif;
  }
  .canvas { position: relative; width: 900px; height: 1200px; }

  .card {
    position: absolute;
    border-radius: 18px;
    overflow: hidden;
    box-shadow: 0 6px 16px rgba(0,0,0,0.25);
  }
  .card-front { left: 78px; top: 136px; width: 762px; height: 434px; background: var(--paper); }
  .card-back  { left: 76px; top: 630px; width: 767px; height: 436px; background: var(--brand-blue); }

  .front-bands { position: absolute; inset: 0; }

  .front-logo {
    position: absolute; left: 30px; top: 40px; width: 310px;
    text-align: center;
  }
  .logo-dot {
    width: 114px; height: 114px; border-radius: 50%;
    background: var(--brand-orange);
    margin: 0 auto 12px;
  }
  .logo-name {
    color: var(--brand-blue); font-weight: 700;
    font-size: 28px; line-height: 1.05; letter-spacing: 0.5px;
  }

  .holder {
    position: absolute; right: 40px; top: 64px; text-align: right; color: var(--white);
  }
  .holder-name { font-weight: 700; font-size: 31px; line-height: 1.2; }
  .holder-role { font-size: 23px; line-height: 1.3; }

  .contacts {
    position: absolute; left: 42px; top: 294px; list-style: none;
    color: var(--ink); font-size: 21px;
  }
  .contacts li { display: flex; align-items: center; height: 37px; }
  .contacts svg { width: 22px; height: 22px; margin-right: 13px; flex: none; }
  .icon-fill { fill: var(--brand-blue); }
  .icon-line { fill: none; stroke: var(--brand-blue); stroke-width: 2; }

  .socials { position: absolute; left: 548px; top: 354px; display: flex; gap: 16px; }
  .social-dot {
    width: 46px; height: 46px; border-radius: 50%;
    background: var(--brand-blue); border: 3px solid var(--white);
  }

  .back-logo { position: absolute; left: 0; right: 0; top: 70px; text-align: center; }
  .back-logo .logo-dot { width: 204px; height: 204px; margin-bottom: 16px; }
  .back-name { color: var(--white); font-weight: 700; font-size: 56px; line-height: 1.0; }
  .back-name .second-line { display: block; font-size: 36px; letter-spacing: 12px; margin-top: 8px; }
</style>
</head>
<body>
<main class="canvas">

  <section class="card card-front" aria-label="Business card front">
    <svg class="front-bands" viewBox="0 0 762 434" width="762" height="434" aria-hidden="true">
      <polygon points="317,0 762,0 762,212 420,212" fill="var(--brand-blue)"/>
      <polygon points="423,218 762,218 762,434 528,434" fill="var(--brand-orange)"/>
    </svg>

    <div class="front-logo">
      <div class="logo-dot"></div>
      <p class="logo-name">BRIGHT LANTERN<br>COLLECTIVE</p>
    </div>

    <div class="holder">
      <p class="holder-name">Mathéo VRANEL</p>
      <p class="holder-role">Founder &amp; CEO</p>
    </div>

    <ul class="contacts">
      <li>
        <svg viewBox="0 0 24 24" aria-hidden="true"><path class="icon-fill" d="M6.6 10.8a15 15 0 0 0 6.6 6.6l2.2-2.2a1 1 0 0 1 1-.25 11.4 11.4 0 0 0 3.6.57 1 1 0 0 1 1 1V20a1 1 0 0 1-1 1A17 17 0 0 1 3 4a1 1 0 0 1 1-1h3.5a1 1 0 0 1 1 1c0 1.25.2 2.45.57 3.57a1 1 0 0 1-.25 1z"/></svg>
        +590 690 482 517
      </li>
      <li>
        <svg viewBox="0 0 24 24" aria-hidden="true"><path class="icon-fill" d="M2 6.5V19h20V6.5l-10 7.5z M3 5l9 6.8L21 5z"/></svg>
        ceo@brightlanterncollective.com
      </li>
      <li>
        <svg viewBox="0 0 24 24" aria-hidden="true"><g class="icon-line"><circle cx="12" cy="12" r="9"/><ellipse cx="12" cy="12" rx="4" ry="9"/><path d="M3 12h18M5 7h14M5 17h14"/></g></svg>
        www.brightlanterncollective.com
      </li>
    </ul>

    <div class="socials" aria-hidden="true">
      <span class="social-dot"></span>
      <span class="social-dot"></span>
      <span class="social-dot"></span>
    </div>
  </section>

  <section class="card card-back" aria-label="Business card back">
    <div class="back-logo">
      <div class="logo-dot"></div>
      <p class="back-name">BRIGHT LANTERN<span class="second-line">COLLECTIVE</span></p>
    </div>
  </section>

</main>
</body>
</html>
```